wisdom by sparks community

The website presents a new interactive learning system where it provides not only the teaching material as the instructor friend who can both teach and learn, making friends and making money.
Make friends and get money.

Learn

```html
<!DOCTYPE html>
<html lang="en">
<head>
<meta charset="utf-8">
<title>Wisdom by Sparks Community</title>
<link href="https://fonts.googleapis.com/css2?family=Open+Sans:wght@400;600;700&family=Roboto+Condensed:wght@300;400;700&display=swap" rel="stylesheet">
<style>
:root{
  --blue:#0f5190;
  --blue-deep:#0b3f74;
  --navy:#0d4a86;
  --footer:#0a3d6e;
  --ink:#555b63;
  --ink-dark:#3d4349;
  --grey-head:#6b6f74;
  --rule:#c9ced4;
  --light:#f0f0f0;
  --white:#ffffff;
}
*{margin:0;padding:0;box-sizing:border-box}
html,body{width:1200px;height:2651px;overflow:hidden}
body{font-family:"Open Sans",Arial,sans-serif;color:var(--ink);background:var(--white);position:relative}
.section{position:absolute;left:0;width:1200px}
.wrap{position:absolute;left:122px;width:956px}

/* hero */
.hero{top:0;height:592px;overflow:hidden}
.hero-photo{position:absolute;inset:0;background:
  radial-gradient(ellipse 420px 360px at 860px 330px,rgba(120,150,190,.55),transparent 70%),
  radial-gradient(ellipse 300px 260px at 420px 430px,rgba(90,130,180,.45),transparent 70%),
  linear-gradient(100deg,#1d4f8a 0%,#2b5d98 40%,#3a6aa2 60%,#24508a 100%)}
.brand{position:absolute;left:122px;top:30px;display:flex;align-items:center;color:var(--white);font-family:"Open Sans",Arial,sans-serif;font-weight:600;font-size:16px;letter-spacing:.3px}
.brand-mark{width:12px;height:12px;background:var(--white);margin-right:10px}
.nav{position:absolute;top:33px;left:432px;display:flex;font-size:11.5px;color:#dce6f2;letter-spacing:.3px}
.nav span{margin-right:11px}
.nav .sep{opacity:.7}
.nav .active{color:var(--white);font-weight:700}
.account{position:absolute;top:31px;left:948px;color:var(--white);font-weight:700;font-size:13px}
.account span{margin-right:30px}
.hero h1{position:absolute;left:122px;top:185px;color:var(--white);font-weight:600;font-size:35px;letter-spacing:.4px}
.hero p{position:absolute;left:122px;top:258px;width:420px;color:var(--white);font-size:13.5px;line-height:24px}
.btn-outline{position:absolute;left:122px;top:378px;width:150px;height:38px;border:1px solid var(--white);color:var(--white);font-size:12px;font-weight:600;display:flex;align-items:center;justify-content:center}
.hero-call{position:absolute;left:288px;top:382px;color:var(--white);font-size:20px}
.hero-call b{font-weight:700}

/* welcome */
.welcome{top:592px;height:268px}
.sec-title{font-family:"Roboto Condensed",sans-serif;font-size:23px;color:var(--grey-head);text-transform:uppercase}
.sec-title em{font-style:normal;color:var(--blue)}
.rule{width:176px;height:4px;background:var(--rule);margin-top:10px}
.body-text{font-size:14px;line-height:26.5px;color:var(--ink)}
.welcome .body-text{margin-top:22px}
.more-arrow{margin-top:4px}

/* features */
.feature{height:330px;overflow:hidden}
.feature-a{top:860px}
.feature-b{top:1190px}
.feature svg.shape{position:absolute;top:0;left:0}
.feature-copy{position:absolute;width:460px}
.feature-title{font-family:"Roboto Condensed",sans-serif;font-size:19px;color:var(--blue);text-transform:uppercase}
.feature .body-text{margin-top:20px}
.btn-solid{display:inline-flex;align-items:center;justify-content:center;width:131px;height:35px;background:var(--blue);color:var(--white);font-size:13px;font-weight:600;margin-top:26px}
.feature-b .feature-copy{text-align:right}
.feature-b .rule{margin-left:auto}

/* blog */
.blog{top:1520px;height:327px;background:var(--light)}
.blog .sec-title{position:absolute;left:122px;top:42px}
.blog .rule{position:absolute;left:122px;top:82px;margin:0}
.card{position:absolute;top:107px;width:298px;height:193px;background:var(--white)}
.card-side{position:absolute;left:0;top:0;width:55px;height:148px}
.date{width:55px;height:55px;background:var(--blue);color:var(--white);text-align:center;font-weight:700;font-size:11px;line-height:13px;padding-top:7px}
.meta{text-align:center;font-size:10px;color:var(--ink-dark);margin-top:12px}
.meta div{margin-bottom:6px}
.card-photo{position:absolute;left:55px;top:0;width:243px;height:148px}
.card-text{position:absolute;left:55px;top:153px;width:243px;font-size:12px;line-height:17px;color:var(--ink-dark)}

/* cta */
.cta{top:1847px;height:155px;overflow:hidden}
.cta-photo{position:absolute;inset:0;background:
  radial-gradient(ellipse 300px 120px at 200px 80px,rgba(150,170,200,.35),transparent 70%),
  radial-gradient(ellipse 300px 120px at 950px 70px,rgba(150,170,200,.3),transparent 70%),
  linear-gradient(90deg,#2c4f7c,#3b5f8e 50%,#2a4a76)}
.cta h2{position:absolute;left:200px;top:52px;color:var(--white);font-family:"Roboto Condensed",sans-serif;font-weight:300;font-size:37px;letter-spacing:-.2px}
.cta-btn{position:absolute;left:844px;top:56px;width:152px;height:41px;background:var(--white);color:var(--blue);font-family:"Roboto Condensed",sans-serif;font-size:20px;display:flex;align-items:center;justify-content:center}

/* testimonials */
.testimonials{top:2002px;height:392px;text-align:center}
.testimonials .sec-title{position:absolute;left:0;width:1200px;top:38px}
.testimonials .rule{position:absolute;left:512px;top:84px;margin:0}
.quote{position:absolute;left:300px;width:600px;top:104px;font-size:14px;line-height:27px;color:var(--ink)}
.avatar{position:absolute;left:542px;top:180px;width:116px;height:116px;border-radius:50%;border:4px solid #e5e7ea;background:radial-gradient(circle at 50% 45%,#8a7468,#3a302c 75%)}
.client{position:absolute;left:0;width:1200px;top:316px;color:var(--blue);font-size:14px;font-weight:600}
.position{position:absolute;left:0;width:1200px;top:338px;font-size:13px;color:#8a8f95}
.slide-arrow{position:absolute;top:2221px;width:28px;height:28px;border:1px solid #d0d3d7;background:var(--white)}

/* contact */
.contact{top:2394px;height:207px;background:var(--navy);color:var(--white)}
.contact h2{position:absolute;left:0;width:1200px;text-align:center;top:38px;font-family:"Roboto Condensed",sans-serif;font-size:22px;font-weight:400}
.contact .bar{position:absolute;left:512px;top:76px;width:176px;height:4px;background:#0a3a68}
.info{position:absolute;top:130px;display:flex}
.info svg{margin-right:12px;flex:none}
.info-label{font-family:"Roboto Condensed",sans-serif;font-weight:700;font-size:16px}
.info-val{font-size:13px;color:#b6cbe2;line-height:17px;margin-top:3px}
.footer{top:2601px;height:50px;background:var(--footer);font-size:12px;color:#7f9cbc}
.footer .left{position:absolute;left:122px;top:17px}
.footer .left b{color:#c5d5e6;font-weight:600}
.footer .right{position:absolute;right:122px;top:17px}
</style>
</head>
<body>

<section class="section hero">
  <div class="hero-photo" role="img" aria-label="Photo of an instructor helping students at computers, tinted blue"></div>
  <div class="brand"><span class="brand-mark"></span>Wisdom by Sparks Community</div>
  <nav class="nav">
    <span class="active">HOME</span><span class="sep">/</span>
    <span>ABOUT US</span><span class="sep">/</span>
    <span>FEATURES</span><span class="sep">/</span>
    <span>PRICING</span><span class="sep">/</span>
    <span>BLOG</span><span class="sep">/</span>
    <span>CONTACT US</span>
  </nav>
  <div class="account"><span>LOG IN</span>SIGN-UP</div>
  <h1>MAKE FRIENDS AND GET MONEY</h1>
  <p>Lorem ipsum dolor sit amet, consectetur adipiscing elit. Nullam fermentum ante facilisis leo lacinia, a dignissim orci eleifend. Donec id justo sed elit porttitor.</p>
  <div class="btn-outline">Free Register Now!</div>
  <div class="hero-call">Or Call : <b>555 010 24680</b></div>
</section>

<section class="section welcome">
  <div class="wrap" style="top:35px">
    <h2 class="sec-title">Welcome to <em>Wisdom by Sparks Community</em></h2>
    <div class="rule"></div>
    <p class="body-text">Lorem ipsum dolor sit amet, consectetur adipiscing elit. Nullam fermentum ante facilisis leo lacinia, a dignissim orci eleifend. Donec id justo sed elit tempor pellentesque. Praesent sollicitudin rhoncus massa. Pellentesque habitant morbi tristique senectus et netus et malesuada fames ac turpis egestas. Curabitur scelerisque auctor erat faucibus porttitor. Suspendisse tincidunt justo eget nisi posuere cursus. Pellentesque quam enim, pharetra ac ante eu, congue eleifend diam. Aliquam sit amet nisl ex. Vestibulum sed maximus ipsum. Donec dignissim ultrices nibh, interdum venenatis felis ultrices eget. Vivamus blandit a purus vitae faucibus.</p>
    <svg class="more-arrow" width="20" height="10" viewBox="0 0 20 10"><path d="M0 5h17M13 1l4 4-4 4" stroke="#0f5190" stroke-width="2" fill="none"/></svg>
  </div>
</section>

<section class="section feature feature-a">
  <svg class="shape" width="1200" height="330" role="img" aria-label="Illustration of a light bulb over a rain cloud on a blue blueprint grid">
    <defs><radialGradient id="gA" cx="70%" cy="45%" r="60%"><stop offset="0" stop-color="#2a73bf"/><stop offset="1" stop-color="#0f5190"/></radialGradient></defs>
    <polygon points="707,0 1200,0 1200,330 601,330" fill="url(#gA)"/>
  </svg>
  <div class="feature-copy" style="left:122px;top:26px">
    <h3 class="feature-title">Wisdom by Sparks Community</h3>
    <div class="rule"></div>
    <p class="body-text">Lorem ipsum dolor sit amet, consectetur adipiscing elit. Nullam fermentum ante facilisis leo lacinia, a dignissim or lorem ifend. Donec id justo sed elit tempor pellentesque. Praesent sollicdin rhoncus massa. Pellentesque habitant morbi tristique senectus et netus et malesuada fames ac turpis egestas. Scrisque auctor erat faucibus porttitor.</p>
    <div class="btn-solid">READ MORE</div>
  </div>
</section>

<section class="section feature feature-b">
  <svg class="shape" width="1200" height="330" role="img" aria-label="Illustration of a light bulb and cloud linked to speech drops showing partner examples on a blue grid">
    <defs><radialGradient id="gB" cx="30%" cy="45%" r="60%"><stop offset="0" stop-color="#2a73bf"/><stop offset="1" stop-color="#0f5190"/></radialGradient></defs>
    <polygon points="0,0 601,0 495,330 0,330" fill="url(#gB)"/>
  </svg>
  <div class="feature-copy" style="left:618px;top:24px">
    <h3 class="feature-title">Wisdom by Sparks Community</h3>
    <div class="rule"></div>
    <p class="body-text">Lorem ipsum dolor sit amet, consectetur adipiscing elit. Nullam fermentum ante facilisis leo lacinia, a dignissim or lorem ifend. Donec id justo sed elit tempor pellentesque. Praesent sollicdin rhoncus massa. Pellentesque habitant morbi tristique senectus et netus et malesuada fames ac turpis egestas. Scrisque auctor erat faucibus porttitor.</p>
    <div class="btn-solid">READ MORE</div>
  </div>
</section>

<section class="section blog">
  <h2 class="sec-title">Our Latest <em>Blog</em></h2>
  <div class="rule"></div>

  <article class="card" style="left:122px">
    <div class="card-side">
      <div class="date">03<br>OCT<br>2014</div>
      <div class="meta">
        <div><svg width="18" height="16" viewBox="0 0 18 16"><path d="M1 1h16v10H7l-4 4v-4H1z" fill="none" stroke="#555" stroke-width="1.3"/><path d="M9 3v6M6 6h6" stroke="#555" stroke-width="1.3"/></svg></div>
        <div><svg width="18" height="16" viewBox="0 0 18 16"><path d="M9 15S1 10 1 5a4 4 0 0 1 8-1 4 4 0 0 1 8 1c0 5-8 10-8 10z" fill="none" stroke="#555" stroke-width="1.3"/></svg><br>20</div>
      </div>
    </div>
    <div class="card-photo" role="img" aria-label="Photo of a student studying with a laptop" style="background:linear-gradient(120deg,#e8d6cf,#c9a7a3 45%,#d9c1c6)"></div>
    <p class="card-text">Lorem ipsum dolor sit amet consectetur adipiscing elit. Cras nec felis ut orci.</p>
  </article>

  <article class="card" style="left:452px">
    <div class="card-side">
      <div class="date">03<br>OCT<br>2014</div>
      <div class="meta">
        <div><svg width="18" height="16" viewBox="0 0 18 16"><path d="M1 1h16v10H7l-4 4v-4H1z" fill="none" stroke="#555" stroke-width="1.3"/><path d="M9 3v6M6 6h6" stroke="#555" stroke-width="1.3"/></svg></div>
        <div><svg width="18" height="16" viewBox="0 0 18 16"><path d="M9 15S1 10 1 5a4 4 0 0 1 8-1 4 4 0 0 1 8 1c0 5-8 10-8 10z" fill="none" stroke="#555" stroke-width="1.3"/></svg><br>20</div>
      </div>
    </div>
    <div class="card-photo" role="img" aria-label="Photo of a smiling student at a desk" style="background:linear-gradient(120deg,#f2eee9,#e1cfc4 45%,#c8b0a4)"></div>
    <p class="card-text">Lorem ipsum dolor sit amet consectetur adipiscing elit. Cras nec felis ut orci.</p>
  </article>

  <article class="card" style="left:783px">
    <div class="card-side">
      <div class="date">03<br>OCT<br>2014</div>
      <div class="meta">
        <div><svg width="18" height="16" viewBox="0 0 18 16"><path d="M1 1h16v10H7l-4 4v-4H1z" fill="none" stroke="#555" stroke-width="1.3"/><path d="M9 3v6M6 6h6" stroke="#555" stroke-width="1.3"/></svg></div>
        <div><svg width="18" height="16" viewBox="0 0 18 16"><path d="M9 15S1 10 1 5a4 4 0 0 1 8-1 4 4 0 0 1 8 1c0 5-8 10-8 10z" fill="none" stroke="#555" stroke-width="1.3"/></svg><br>20</div>
      </div>
    </div>
    <div class="card-photo" role="img" aria-label="Photo of a smiling professional woman" style="background:linear-gradient(120deg,#b8ccd6,#dfe6ea 50%,#c4d3db)"></div>
    <p class="card-text">Lorem ipsum dolor sit amet consectetur adipiscing elit. Cras nec felis ut orci.</p>
  </article>
</section>

<section class="section cta">
  <div class="cta-photo" role="img" aria-label="Blurred photo of a crowd, tinted blue"></div>
  <h2>GET STARTED INVITATION FRIEND TODAY</h2>
  <div class="cta-btn">SIGN IN NOW</div>
</section>

<section class="section testimonials">
  <h2 class="sec-title">Client's <em>Testimonials</em></h2>
  <div class="rule"></div>
  <p class="quote">Lorem ipsum dolor sit amet, colo amet nsectetur adipiscing elit. In metus vehicula lacus consectetur venenatis nec a leo.</p>
  <div class="avatar" role="img" aria-label="Client portrait photo"></div>
  <div class="client">CLIENT NAME</div>
  <div class="position">Position</div>
</section>
<svg class="slide-arrow" style="left:122px" viewBox="0 0 28 28"><path d="M16 8l-6 6 6 6" fill="none" stroke="#9aa0a6" stroke-width="2"/></svg>
<svg class="slide-arrow" style="left:1050px" viewBox="0 0 28 28"><path d="M12 8l6 6-6 6" fill="none" stroke="#9aa0a6" stroke-width="2"/></svg>

<section class="section contact">
  <h2>CONTACT US</h2>
  <div class="bar"></div>

  <div class="info" style="left:122px">
    <svg width="36" height="36" viewBox="0 0 36 36"><path d="M18 3a10 10 0 0 0-10 10c0 8 10 20 10 20s10-12 10-20A10 10 0 0 0 18 3z" fill="#5f86b0"/><circle cx="18" cy="13" r="4" fill="#0d4a86"/></svg>
    <div><div class="info-label">ADDRESS</div><div class="info-val">Elm Rise, 48 Harbor Lane<br>Street, Northvale, 0456 Westshire</div></div>
  </div>

  <div class="info" style="left:458px">
    <svg width="40" height="36" viewBox="0 0 40 36"><path d="M4 12c0-5 32-5 32 0v4h-8v-3H12v3H4z" fill="#5f86b0"/><rect x="9" y="18" width="22" height="15" rx="3" fill="#5f86b0"/><circle cx="20" cy="25" r="4" fill="#0d4a86"/></svg>
    <div><div class="info-label">CALL</div><div class="info-val">555 010 246800</div></div>
  </div>

  <div class="info" style="left:696px">
    <svg width="40" height="36" viewBox="0 0 40 36"><rect x="11" y="3" width="18" height="11" fill="#5f86b0"/><rect x="3" y="13" width="34" height="18" rx="2" fill="#5f86b0"/><rect x="10" y="24" width="20" height="9" fill="#8fadcc"/></svg>
    <div><div class="info-label">FAX</div><div class="info-val">555 010 24680</div></div>
  </div>

  <div class="info" style="left:912px">
    <svg width="38" height="36" viewBox="0 0 38 36"><rect x="3" y="8" width="32" height="22" fill="#5f86b0"/><path d="M3 8l16 13 16-13" fill="none" stroke="#0d4a86" stroke-width="2"/></svg>
    <div><div class="info-label">EMAIL</div><div class="info-val">info@wisdomsparks.example</div></div>
  </div>
</section>

<footer class="section footer">
  <div class="left">Copyright © 2014 <b>Sparks Community</b>. All right reserved.</div>
  <div class="right">Terms Of Service | Privacy Policy</div>
</footer>

</body>
</html>
```